Hero Image Redesign for VELM Consulting Website

About us:
VELM Consulting is an organisational psychology and human resource management consulting firm based in Melbourne, Australia (www.velmadvisory-example.com.au). We are a B2B offering a range of organisational psychology measurement and consulting. The largest part of our business is our online psychometric assessments, which are self-managed via an online portal, which is currently used by many organisations worldwide as part of their recruitment process.

What we are looking for:
We are seeking assistance to redesign an image located above the fold - on the top right hand side of homepage. We want an image of a small group of diverse people happily working together using a laptop (either individually or as a group), overlayed with graphic representations reflective of using our online Psychometric Assessment tool, in an interactive fashion.

The graphics will highlight key features of the self-service VELM Psychometric Assessment Portal, specifically ease of use, flexibility and our integrated approach. We want the image to look clean, clear, minimal, with use of negative space. All graphics must be accessible (including sufficient colour contrast and text size).

We would like the graphic to feature 3 “pop ups” highlighting features, and these should appear over the image:

1. Setup participants easily online
2. Check the status of an assessment
3. View participants’ reports

Examples from other SaaS websites attached.

The final design should communicate trust, reliability, our scientific evidence based approach, and our approachable and friendly customer service.

Our main brand colours are:
• Navy – HEX #2F2971
• Mid Blue – HEX #0C75C0
• Black – HEX #000000

About VELM’ website and potential for future work:

• VELM’ website pages have been created using Bricks Builder for WordPress.
• There is a strong possibility of future projects following successful delivery. We are an excellent client – ethical, professional and with a genuine commitment to partnership.

Need extra days to review

```html
<!DOCTYPE html>
<html lang="en">
<head>
<meta charset="utf-8">
<title>VELM Consulting — Organisational Psychology Consulting hero banners</title>
<link href="https://fonts.googleapis.com/css2?family=Outfit:wght@400;500&family=Montserrat:wght@400;500&family=Caveat:wght@500&display=swap" rel="stylesheet">
<style>
  :root{
    --navy:#2F2971;
    --mid-blue:#0C75C0;
    --black:#000000;
    --cream:#F6F2EE;
    --white:#FFFFFF;
    --ink:#111111;
    --body-ink:#2a2a2a;
  }
  *{box-sizing:border-box;margin:0;padding:0}
  html,body{width:714px;height:1200px;overflow:hidden;background:var(--white)}
  body{position:relative;font-family:"Montserrat",sans-serif}

  .hero{position:absolute;left:20px;width:673px;height:379px;background:var(--cream);overflow:hidden}
  .hero--navy-1{top:16px;--accent:var(--navy)}
  .hero--black{top:408px;--accent:var(--black)}
  .hero--navy-2{top:801px;--accent:var(--navy)}

  .hero__chart{position:absolute;inset:0;width:673px;height:379px}

  .hero__title{position:absolute;left:42px;top:56px;font-family:"Outfit",sans-serif;font-weight:500;font-size:40.5px;line-height:38px;letter-spacing:-0.6px;color:var(--ink)}
  .hero__lead{position:absolute;left:42px;top:193px;width:250px;font-size:11px;line-height:13.5px;color:var(--body-ink)}
  .hero__actions{position:absolute;left:42px;top:255px;display:flex;gap:14px}
  .btn{display:flex;align-items:center;justify-content:center;width:104px;height:31px;border-radius:16px;font-size:8px;font-weight:500;color:var(--white);text-decoration:none}
  .btn--primary{background:var(--mid-blue)}
  .btn--secondary{background:var(--accent)}

  .hero__photo{position:absolute;border-radius:120px 120px 0 0}

  .popup{position:absolute;display:flex;align-items:flex-start;gap:7px;border-radius:8px;font-family:"Outfit",sans-serif;font-size:13px;line-height:15.5px;padding:8px 9px}
  .popup svg{flex:none;margin-top:1px}
  .popup--status{background:var(--black);color:var(--white);width:111px;height:58px;font-size:12px;line-height:13.5px;padding:8px 7px}
  .popup--setup{background:var(--mid-blue);color:var(--white);width:134px;height:58px;padding:7px 8px}
  .popup--reports{background:rgba(255,255,255,.94);color:var(--ink);width:128px;height:59px;padding:7px 8px}

  .note{position:absolute;font-family:"Caveat",cursive;font-size:11px;line-height:10px;color:var(--ink);white-space:nowrap}
  .note--light{color:var(--white)}
</style>
</head>
<body>

<!-- Banner 1 -->
<section class="hero hero--navy-1">
  <svg class="hero__chart" viewBox="0 0 673 379" aria-hidden="true">
    <defs>
      <pattern id="grid-light-1" width="20" height="20" patternUnits="userSpaceOnUse">
        <path d="M20 0V20M0 20H20" stroke="rgba(255,255,255,.13)" stroke-width="0.7" fill="none"/>
      </pattern>
    </defs>
    <path d="M70 379L178 327L224 348L334 282L379 313L450 280L560 150L595 120L630 160L673 212V379Z" fill="var(--navy)"/>
    <path d="M70 379L178 327L224 348L334 282L379 313L450 280L560 150L595 120L630 160L673 212V379Z" fill="url(#grid-light-1)"/>
    <path d="M593 169L673 155V181L644 239Z" fill="var(--mid-blue)"/>
    <ellipse cx="331" cy="285" rx="38" ry="10" transform="rotate(-10 331 285)" fill="none" stroke="var(--mid-blue)" stroke-width="2"/>
  </svg>

  <h1 class="hero__title">Organisational<br>Psychology<br>Consulting</h1>
  <p class="hero__lead">Optimise your workforce with psychometric testing, engagement surveys, wellbeing measures, and organisational development.</p>
  <div class="hero__actions">
    <a class="btn btn--primary" href="#">Psychometric Testing</a>
    <a class="btn btn--secondary" href="#">Speak to an Expert</a>
  </div>

  <div class="hero__photo" role="img" aria-label="Photo of a smiling professional in a blue suit jacket" style="left:432px;top:60px;width:236px;height:319px;background:linear-gradient(180deg,#6b4a3a 0%,#4c3a33 28%,#2d56a0 45%,#1f3f82 100%)"></div>

  <div class="popup popup--setup" style="left:334px;top:129px">
    <svg width="18" height="18" viewBox="0 0 18 18"><circle cx="9" cy="9" r="9" fill="var(--white)"/><path d="M5 9.3l2.7 2.6L13 6.4" stroke="var(--mid-blue)" stroke-width="1.8" fill="none" stroke-linecap="round" stroke-linejoin="round"/></svg>
    <span>Setup<br>participants<br>easily online</span>
  </div>
  <div class="popup popup--status" style="left:536px;top:42px">
    <svg width="20" height="20" viewBox="0 0 20 20"><circle cx="10" cy="10" r="10" fill="var(--white)"/><path d="M10 10V4A6 6 0 1 1 4 10Z" fill="var(--black)"/></svg>
    <span>Check the<br>status of an<br>assessment</span>
  </div>
  <div class="popup popup--reports" style="left:380px;top:241px">
    <svg width="19" height="20" viewBox="0 0 19 20"><rect width="19" height="20" rx="3" fill="var(--navy)"/><path d="M5 7H14M5 10.5H14M5 14H11" stroke="var(--white)" stroke-width="1.4" stroke-linecap="round"/></svg>
    <span>View<br>participants’<br>reports</span>
  </div>

  <span class="note" style="left:373px;top:209px;transform:rotate(-4deg)">Ease of use</span>
  <span class="note note--light" style="left:364px;top:334px;transform:rotate(-14deg);text-align:center">Integrated<br>Approach</span>
  <span class="note note--light" style="left:578px;top:145px;transform:rotate(12deg)">Flexibility</span>
</section>

<!-- Banner 2 -->
<section class="hero hero--black">
  <svg class="hero__chart" viewBox="0 0 673 379" aria-hidden="true">
    <defs>
      <pattern id="grid-light-2" width="20" height="20" patternUnits="userSpaceOnUse">
        <path d="M20 0V20M0 20H20" stroke="rgba(255,255,255,.15)" stroke-width="0.7" fill="none"/>
      </pattern>
    </defs>
    <path d="M73 379L180 327L225 348L330 286L440 230L560 158L597 120L650 180L673 200V379Z" fill="var(--black)"/>
    <path d="M73 379L180 327L225 348L330 286L440 230L560 158L597 120L650 180L673 200V379Z" fill="url(#grid-light-2)"/>
    <path d="M595 194L673 183V213L642 275Z" fill="var(--mid-blue)"/>
    <ellipse cx="184" cy="323" rx="38" ry="10" transform="rotate(-10 184 323)" fill="none" stroke="var(--mid-blue)" stroke-width="2"/>
  </svg>

  <h1 class="hero__title" style="left:44px">Organisational<br>Psychology<br>Consulting</h1>
  <p class="hero__lead" style="left:44px">Optimise your workforce with psychometric testing, engagement surveys, wellbeing measures, and organisational development.</p>
  <div class="hero__actions" style="left:44px">
    <a class="btn btn--primary" href="#">Psychometric Testing</a>
    <a class="btn btn--secondary" href="#">Speak to an Expert</a>
  </div>

  <div class="hero__photo" role="img" aria-label="Photo of a smiling young man in a checked shirt holding an open laptop" style="left:318px;top:36px;width:292px;height:343px;border-radius:120px 120px 0 0;background:linear-gradient(180deg,#3a2c26 0%,#c79a82 22%,#5b5d63 45%,#6b6b6d 70%,#4a4a4c 100%)"></div>

  <div class="popup popup--setup" style="left:350px;top:128px">
    <svg width="18" height="18" viewBox="0 0 18 18"><circle cx="9" cy="9" r="9" fill="var(--white)"/><path d="M5 9.3l2.7 2.6L13 6.4" stroke="var(--mid-blue)" stroke-width="1.8" fill="none" stroke-linecap="round" stroke-linejoin="round"/></svg>
    <span>Setup<br>participants<br>easily online</span>
  </div>
  <div class="popup popup--status" style="left:531px;top:51px;width:119px">
    <svg width="20" height="20" viewBox="0 0 20 20"><circle cx="10" cy="10" r="10" fill="var(--white)"/><path d="M10 10V4A6 6 0 1 1 4 10Z" fill="var(--black)"/></svg>
    <span>Check the<br>status of an<br>assessment</span>
  </div>
  <div class="popup popup--reports" style="left:511px;top:240px">
    <svg width="19" height="20" viewBox="0 0 19 20"><rect width="19" height="20" rx="3" fill="var(--navy)"/><path d="M5 7H14M5 10.5H14M5 14H11" stroke="var(--white)" stroke-width="1.4" stroke-linecap="round"/></svg>
    <span>View<br>participants’<br>reports</span>
  </div>

  <span class="note" style="left:415px;top:84px;transform:rotate(12deg)">Flexibility</span>
  <span class="note" style="left:369px;top:215px;transform:rotate(-4deg)">Ease of use</span>
  <span class="note note--light" style="left:567px;top:160px;transform:rotate(-14deg);text-align:center">Integrated<br>Approach</span>
</section>

<!-- Banner 3 -->
<section class="hero hero--navy-2">
  <svg class="hero__chart" viewBox="0 0 673 379" aria-hidden="true">
    <defs>
      <pattern id="grid-light-3" width="20" height="20" patternUnits="userSpaceOnUse">
        <path d="M20 0V20M0 20H20" stroke="rgba(255,255,255,.13)" stroke-width="0.7" fill="none"/>
      </pattern>
    </defs>
    <path d="M70 379L178 327L224 348L334 282L379 313L450 285L560 240L673 205V379Z" fill="var(--navy)"/>
    <path d="M70 379L178 327L224 348L334 282L379 313L450 285L560 240L673 205V379Z" fill="url(#grid-light-3)"/>
    <path d="M624 164L673 157V183L648 241Z" fill="var(--mid-blue)"/>
    <ellipse cx="331" cy="285" rx="38" ry="10" transform="rotate(-10 331 285)" fill="none" stroke="var(--mid-blue)" stroke-width="2"/>
  </svg>

  <h1 class="hero__title">Organisational<br>Psychology<br>Consulting</h1>
  <p class="hero__lead">Optimise your workforce with psychometric testing, engagement surveys, wellbeing measures, and organisational development.</p>
  <div class="hero__actions">
    <a class="btn btn--primary" href="#">Psychometric Testing</a>
    <a class="btn btn--secondary" href="#">Speak to an Expert</a>
  </div>

  <div class="hero__photo" role="img" aria-label="Photo of a smiling woman with curly hair and glasses in a pink blazer" style="left:422px;top:80px;width:236px;height:299px;background:linear-gradient(180deg,#2a1d17 0%,#3b2a22 30%,#8a5a44 45%,#e8c2b6 62%,#f2f0ee 100%)"></div>

  <div class="popup popup--setup" style="left:337px;top:132px">
    <svg width="18" height="18" viewBox="0 0 18 18"><circle cx="9" cy="9" r="9" fill="var(--white)"/><path d="M5 9.3l2.7 2.6L13 6.4" stroke="var(--mid-blue)" stroke-width="1.8" fill="none" stroke-linecap="round" stroke-linejoin="round"/></svg>
    <span>Setup<br>participants<br>easily online</span>
  </div>
  <div class="popup popup--status" style="left:537px;top:42px">
    <svg width="20" height="20" viewBox="0 0 20 20"><circle cx="10" cy="10" r="10" fill="var(--white)"/><path d="M10 10V4A6 6 0 1 1 4 10Z" fill="var(--black)"/></svg>
    <span>Check the<br>status of an<br>assessment</span>
  </div>
  <div class="popup popup--reports" style="left:382px;top:241px">
    <svg width="19" height="20" viewBox="0 0 19 20"><rect width="19" height="20" rx="3" fill="var(--navy)"/><path d="M5 7H14M5 10.5H14M5 14H11" stroke="var(--white)" stroke-width="1.4" stroke-linecap="round"/></svg>
    <span>View<br>participants’<br>reports</span>
  </div>

  <span class="note" style="left:418px;top:82px;transform:rotate(12deg)">Flexibility</span>
  <span class="note" style="left:374px;top:212px;transform:rotate(-4deg)">Ease of use</span>
  <span class="note note--light" style="left:365px;top:334px;transform:rotate(-14deg);text-align:center">Integrated<br>Approach</span>
</section>

</body>
</html>
```